Billboard Design for Modern Dispensary

Hello!
We need a eye-catching 12' x 24' billboard designed for a very successful, modern cannabis dispensary on the Oregon coast, United States. Because of rules, we cannot have any marijuana leafs or other cannabis related images (flower, joints, smoke, etc). We can use the words "Shop" or "Dispensary" - we cannot use the words "cannabis", "marijuana".

Some ideas we had are 3 words stacked on left or center of billboard - maybe across bottom we have horizontal logo and the following words - “North of harbor in Gull Cove”
Another idea is to have a small bubble in bottom/top corner with image of our dog (face only) - with some words around it - like "BONUS Shop Dog" or "Cute Shop Dog" or "Best Shop Dog" or "Friendly Staff"

here's some 3 word examples:
ENJOY
YOUR
TRIP

or

FEEL
GOOD
JUST
AHEAD

or

GOOD
VIBES
ONLY

or

GOOD
TIMES
CHILL
VIBES

I have attached our logo. I have also included a stacked logo version (vertical, not horizontal). the formats are .EPS and .PDF - the logos were created in Affinity Design 2.x.

Our website is coralnook.net if you want to see more images, etc about our dispensary.

Artwork Requirements:
The billboard is 12' tall x 25' wide
The artwork needs to be 1”=1’ @ 300dpi
Please add 6” of bleed all around so your total artwork is 13”x26”
Final deliverable should be .Ai file.

Font styles to use
Sans Serif

Colors
0054AA
0677BA
7BADD7
CADEEF
E8F1F8

Requirements
Nice to have
• See the project description - we included some ideas to consider.
Should not have
• No cannabis images, like flower, cannabis leaves, paraphenlia, cartridges, joints, etc.

```html
<!DOCTYPE html>
<html lang="en">
<head>
<meta charset="utf-8">
<title>Coral Nook – Sleep Better Tonight Billboard</title>
<link rel="stylesheet" href="https://fonts.googleapis.com/css2?family=Lexend:wght@500;700&family=Poppins:wght@700&display=swap">
<style>
  :root {
    --brand-blue: #0559A8;
    --deep-blue: #0054AA;
    --sky-blue: #5A9FD6;
    --paper: #FFFFFF;
    --edge: #C9C9C9;
    --dog-fur: #D9B98A;
    --dog-shadow: #8A7A68;
  }
  * { margin: 0; padding: 0; box-sizing: border-box; }
  html, body { width: 1200px; height: 600px; overflow: hidden; background: var(--paper); }
  .billboard {
    position: relative;
    width: 1200px;
    height: 600px;
    background: var(--paper);
    border: 1px solid var(--edge);
    font-family: "Lexend", sans-serif;
  }
  .hero-panel {
    position: absolute;
    left: 47px;
    top: 23px;
    width: 1106px;
    height: 450px;
    background: var(--brand-blue);
  }
  .headline {
    position: absolute;
    left: 55px;
    top: 120px;
    color: var(--paper);
    font-family: "Lexend", sans-serif;
    font-weight: 500;
    font-size: 72px;
    line-height: 71.5px;
    letter-spacing: -1px;
    text-transform: uppercase;
  }
  .headline span { display: block; }
  .shop-dog {
    position: absolute;
    left: 928px;
    top: 273px;
    width: 130px;
    text-align: center;
  }
  .shop-dog-photo {
    display: block;
    width: 130px;
    height: 130px;
    margin: 0 auto;
  }
  .shop-dog-caption {
    margin-top: 5px;
    color: var(--paper);
    font-family: "Lexend", sans-serif;
    font-weight: 700;
    font-size: 12px;
    letter-spacing: 1.4px;
    white-space: nowrap;
    text-transform: uppercase;
  }
  .footer-band {
    position: absolute;
    left: 47px;
    top: 473px;
    width: 1106px;
    height: 104px;
    background: var(--paper);
    border-left: 1px solid #F2F2F2;
    border-right: 1px solid #F2F2F2;
    border-bottom: 1px solid #F2F2F2;
  }
  .brand {
    position: absolute;
    left: 56px;
    top: 17px;
    display: flex;
    align-items: center;
    gap: 10px;
  }
  .brand-dot {
    width: 58px;
    height: 58px;
    border-radius: 50%;
    border: 3px solid var(--sky-blue);
  }
  .brand-name {
    color: var(--sky-blue);
    font-family: "Lexend", sans-serif;
    font-weight: 500;
    font-size: 27px;
    letter-spacing: 0.5px;
    text-transform: uppercase;
  }
  .location {
    position: absolute;
    right: 42px;
    top: 34px;
    color: var(--deep-blue);
    font-family: "Poppins", sans-serif;
    font-weight: 700;
    font-size: 22px;
    letter-spacing: 0.2px;
    white-space: nowrap;
  }
</style>
</head>
<body>
  <main class="billboard">
    <section class="hero-panel">
      <h1 class="headline">
        <span>Sleep</span>
        <span>Better</span>
        <span>Tonight</span>
      </h1>
      <figure class="shop-dog">
        <svg class="shop-dog-photo" viewBox="0 0 130 130" role="img" aria-label="Photo of the shop dog inside a round bubble">
          <defs>
            <radialGradient id="dogTone" cx="50%" cy="45%" r="55%">
              <stop offset="0%" stop-color="var(--dog-fur)"/>
              <stop offset="75%" stop-color="#B89A74"/>
              <stop offset="100%" stop-color="var(--dog-shadow)"/>
            </radialGradient>
          </defs>
          <circle cx="65" cy="65" r="64" fill="url(#dogTone)"/>
          <circle cx="65" cy="65" r="63.5" fill="none" stroke="#E6E6E6" stroke-width="1"/>
        </svg>
        <figcaption class="shop-dog-caption">Friendly Staff</figcaption>
      </figure>
    </section>
    <footer class="footer-band">
      <div class="brand">
        <span class="brand-dot"></span>
        <span class="brand-name">Coral Nook</span>
      </div>
      <p class="location">North of harbor in Gull Cove</p>
    </footer>
  </main>
</body>
</html>
```